Business Card Design Project

Automotive (vehcle imports & servicing, repairs)business card needed. professional & sleek look needed.

colours same as logo colours pref.

prefer to have few performance logos and Brand names on the card as well.

Target Market(s)

prestige car imports
automotive repairs & service
Automotive compliance workshop

Industry/Entity Type

Automotive

Requirements
Must have
• car brand logos
company details
logo
web address
contact details

```html
<!DOCTYPE html>
<html lang="en">
<head>
<meta charset="utf-8">
<title>Velocity Imports — Business Card</title>
<link rel="stylesheet" href="https://fonts.googleapis.com/css2?family=Exo+2:wght@400;500;600;700&display=swap">
<style>
  :root {
    --red: #d3141c;
    --red-deep: #b80d14;
    --red-light: #e0242b;
    --white: #ffffff;
    --paper: #f7f7f5;
    --ink: #1f1f1f;
    --grey: #555555;
    --stage: #e4e4e4;
    --card-w: 620px;
    --card-h: 354px;
  }
  * { box-sizing: border-box; margin: 0; padding: 0; }
  html, body {
    width: 1200px;
    height: 900px;
    overflow: hidden;
  }
  body {
    background: var(--stage);
    font-family: "Exo 2", "Arial", sans-serif;
    position: relative;
  }
  .card {
    position: absolute;
    width: var(--card-w);
    height: var(--card-h);
    border-radius: 4px;
    overflow: hidden;
    box-shadow: 0 6px 18px rgba(0,0,0,0.12);
  }

  /* Front */
  .card-front {
    left: 110px;
    top: 70px;
    background: linear-gradient(135deg, var(--red-light) 0%, var(--red) 50%, var(--red-deep) 100%);
  }
  .card-front .brand-panel {
    position: absolute;
    left: 232px;
    right: 0;
    top: 118px;
    height: 100px;
    background: var(--paper);
    border-radius: 16px 0 0 16px;
    display: flex;
    align-items: center;
    padding-left: 30px;
    gap: 14px;
  }
  .brand-dot {
    width: 22px;
    height: 22px;
    border-radius: 50%;
    background: var(--red);
    flex: none;
  }
  .brand-name {
    font-weight: 700;
    font-size: 30px;
    letter-spacing: 1px;
    text-transform: uppercase;
    color: var(--red);
    white-space: nowrap;
  }
  .card-front .web-address {
    position: absolute;
    right: 34px;
    bottom: 30px;
    color: var(--white);
    font-size: 15px;
    font-weight: 500;
    letter-spacing: 5px;
  }

  /* Back */
  .card-back {
    left: 470px;
    top: 476px;
    background: var(--paper);
  }
  .holder {
    position: absolute;
    left: 34px;
    top: 40px;
    display: flex;
    align-items: baseline;
    gap: 6px;
  }
  .holder-name {
    color: var(--red);
    font-size: 22px;
    font-weight: 600;
  }
  .holder-role {
    color: var(--grey);
    font-size: 12px;
    font-weight: 500;
  }
  .card-back .brand-panel {
    position: absolute;
    left: 322px;
    right: 0;
    top: 122px;
    height: 92px;
    background: linear-gradient(135deg, var(--red-light), var(--red-deep));
    border-radius: 12px 0 0 12px;
    display: flex;
    align-items: center;
    padding-left: 22px;
    gap: 10px;
  }
  .card-back .brand-dot { background: var(--white); width: 16px; height: 16px; }
  .card-back .brand-name { color: var(--white); font-size: 21px; }
  .contact {
    position: absolute;
    left: 34px;
    bottom: 30px;
    color: var(--ink);
  }
  .contact-address {
    font-size: 15px;
    font-weight: 700;
    margin-bottom: 4px;
  }
  .contact-lines {
    font-size: 13px;
    font-weight: 500;
  }
  .contact-lines .label {
    color: var(--red);
    font-weight: 700;
    margin-right: 3px;
  }
  .contact-lines .item { margin-right: 6px; }
</style>
</head>
<body>

  <section class="card card-front" aria-label="Business card front">
    <div class="brand-panel">
      <span class="brand-dot"></span>
      <span class="brand-name">Velocity Imports</span>
    </div>
    <p class="web-address">velimports.com.au</p>
  </section>

  <section class="card card-back" aria-label="Business card back">
    <div class="holder">
      <span class="holder-name">Daniel Hartley</span>
      <span class="holder-role">| Position</span>
    </div>
    <div class="brand-panel">
      <span class="brand-dot"></span>
      <span class="brand-name">Velocity Imports</span>
    </div>
    <div class="contact">
      <p class="contact-address">PO Box 1234, YourStreer, NY3018.</p>
      <p class="contact-lines">
        <span class="item"><span class="label">P</span>000-123-4567</span>
        <span class="item"><span class="label">F</span>000-123-4568</span>
        <span class="item"><span class="label">E</span>info@velimports.com.au</span>
      </p>
    </div>
  </section>

</body>
</html>
```